Australian Export Wine Label

Brand

To design a label based around Australia’s famous bush ranger Sam Ordway called Ordway’s Run.

Imagery for the label could be an abstract image of Sam’s armour of even of himself or we are open to other possibilities ranging from a traditional label to a more contemporary look and feel.

Images should not include guns and imagery used must be free of copyright.

Designs should be able to be printed by the standard 4 colour print process. As this is not an expensive product there will be no expensive label fiunishes such as gold foil or embossing

The range

The range of wines will consist of a 2011 Shiraz, 2012 Sauvignon Blanc and 2011 Chardonnay.

Market

The primary market for these wines is Ireland with the price range being in the $10-15 bracket. The wines will be available in independent retail shops and restaurants

Front Label Mandatories

1. Front Label: should not exceed 110mm x 80mm

2. Brand name - Ordway’s Run

3. Vintage & Variety – for example 2011 Shiraz

4. Origin – Wine of Australia

5. Text to appear on front label: Born in Co. Antrim, the remarkable Ruth Ordway had eight children including Australia’s most famous Bushranger Sam Ordway. The family’s wild and independent spirit is legendary in country Australia.

Back Label Mandatories

1. Back Label: 80mm x 80mm

2. Brand name

3. Vintage & Variety

4. Alcohol, Volume, Country of production

5. 13.0% VOL 750Ml (must be 4mm in height)

6. Contains egg, milk and nuts. Traces may remain

7. Please include the pregnant lady logo and a recycling logo

8. Wine of Australia

9. Space for barcode

10. Text to appear on back label (Shiraz):

Ordway’s Run is our vineyard named after the Ordway family, whose homestead stood here long before the vines were planted.
Our Ordway’s Run Shiraz is bold and full of flavour. Plums, cassis, chocolate and spice intermingle on the nose and palate, resulting in a full bodied, vibrant wine. Enjoy with a spirit of adventure and a hearty beef stew.

```html
<!DOCTYPE html>
<html lang="en">
<head>
<meta charset="utf-8">
<title>Ordway’s Run Shiraz – Front Label</title>
<link rel="stylesheet" href="https://fonts.googleapis.com/css2?family=Cinzel:wght@400;500&family=Cormorant+Garamond:wght@500;700&family=Source+Sans+3:wght@400&display=swap">
<style>
  :root {
    --backdrop: #5f5f5f;
    --label-paper: #ebe8e3;
    --label-edge: #dcd8d1;
    --wine-red: #7a1d2b;
    --ink: #3b3a39;
    --armour-light: #b9b6b1;
    --armour-dark: #5a5856;
  }
  * { margin: 0; padding: 0; box-sizing: border-box; }
  html, body {
    width: 1200px;
    height: 837px;
    overflow: hidden;
    background: var(--backdrop);
  }
  .canvas {
    position: relative;
    width: 1200px;
    height: 837px;
    display: flex;
    align-items: center;
    justify-content: center;
  }
  .front-label {
    position: relative;
    width: 395px;
    height: 700px;
    background: var(--label-paper);
    border: 1px solid var(--label-edge);
    display: flex;
    flex-direction: column;
    align-items: center;
    text-align: center;
  }
  .armour-artwork {
    margin-top: 88px;
    width: 140px;
    height: 230px;
    background: linear-gradient(160deg, var(--armour-light) 0%, var(--armour-dark) 100%);
    border-radius: 4px;
  }
  .brand-name {
    margin-top: 82px;
    font-family: "Cinzel", serif;
    font-weight: 500;
    font-size: 33px;
    letter-spacing: 0.04em;
    color: var(--wine-red);
    white-space: nowrap;
  }
  .variety {
    margin-top: 26px;
    font-family: "Cormorant Garamond", serif;
    font-weight: 700;
    font-size: 15px;
    letter-spacing: 0.14em;
    color: var(--ink);
  }
  .origin {
    margin-top: 4px;
    font-family: "Cormorant Garamond", serif;
    font-weight: 500;
    font-size: 15px;
    letter-spacing: 0.22em;
    color: var(--ink);
  }
  .vintage {
    margin-top: 3px;
    font-family: "Cormorant Garamond", serif;
    font-weight: 500;
    font-size: 15px;
    letter-spacing: 0.22em;
    color: var(--ink);
  }
  .heritage-story {
    margin-top: 24px;
    width: 290px;
    font-family: "Source Sans 3", sans-serif;
    font-size: 11.5px;
    line-height: 1.75;
    color: var(--ink);
    text-align: left;
  }
</style>
</head>
<body>
  <main class="canvas">
    <section class="front-label">
      <div class="armour-artwork" role="img" aria-label="Etched illustration of a bushranger’s iron armour and helmet"></div>
      <h1 class="brand-name">Ordway’s Run</h1>
      <p class="variety">SHIRAZ</p>
      <p class="origin">WINE OF AUSTRALIA</p>
      <p class="vintage">2011</p>
      <p class="heritage-story">Born in Co. Antrim, the remarkable Ruth Ordway had eight children including Australia’s most famous Bushranger Sam Ordway. The family’s wild and independent spirit is legendary in the country of Australia.</p>
    </section>
  </main>
</body>
</html>
```